Biz Cards, Letterhead
Pls Use Imagination and Refer to Logo Attached. Completely open to ideas. You're the creative ones!
Biz Cards, Letterhead - Consulting
Creative Brief
Simple
Corinne M Dashelt
President & CEO
28516 Belvorne Court Lewes, DE 19958
CDashelt@TheDasheltGroup.example
Don't have to have the text on the back of the card but it is a possibility. Overall, the idea is to be cutting edge, innovative, professional, yet simple. Thanks!
Supply Chain Solutions....Providing Innovation, Automation, & Optimization.

```html
<!DOCTYPE html>
<html lang="en">
<head>
<meta charset="utf-8">
<title>The Dashelt Group — Business Card</title>
<link href="https://fonts.googleapis.com/css2?family=Cormorant+SC:wght@500;600;700&display=swap" rel="stylesheet">
<style>
  :root {
    --backdrop: #eceae6;
    --card: #ffffff;
    --ink: #1f3a8f;
    --ink-deep: #0d1f5c;
    --rule: #2a4496;
    --tab-dark: #0a1747;
    --tab-light: #3c5fd0;
  }
  * { margin: 0; padding: 0; box-sizing: border-box; }
  html, body { width: 1200px; height: 778px; overflow: hidden; }
  body {
    background: var(--backdrop);
    font-family: "Cormorant SC", "Times New Roman", serif;
    color: var(--ink);
    position: relative;
  }
  .card {
    position: absolute;
    left: 168px; top: 132px;
    width: 869px; height: 511px;
    background: var(--card);
    border-radius: 30px;
    box-shadow: 0 6px 18px rgba(0,0,0,0.12);
  }
  .edge-tab {
    position: absolute;
    top: 144px;
    width: 28px; height: 216px;
  }
  .edge-tab--left {
    left: 0;
    border-radius: 0 14px 14px 0;
    background: linear-gradient(90deg, var(--tab-light), var(--tab-dark));
  }
  .edge-tab--right {
    right: 0;
    border-radius: 14px 0 0 14px;
    background: linear-gradient(90deg, var(--tab-dark), var(--tab-light));
  }
  .brand {
    position: absolute;
    left: 0; right: 0; top: 180px;
    text-align: center;
  }
  .brand__rule {
    width: 520px; height: 2px;
    margin: 0 auto;
    background: var(--rule);
  }
  .brand__name {
    font-size: 54px;
    font-weight: 600;
    letter-spacing: 1px;
    line-height: 1;
    padding: 6px 0 8px;
    color: var(--ink);
  }
  .person {
    position: absolute;
    left: 79px; top: 360px;
    width: 320px;
    text-align: center;
  }
  .person__name {
    font-size: 30px;
    font-weight: 500;
    letter-spacing: 0.5px;
    line-height: 1.1;
  }
  .person__title {
    font-size: 19px;
    font-weight: 700;
    color: var(--ink-deep);
    margin-top: 2px;
  }
  .divider {
    position: absolute;
    left: 422px; top: 312px;
    width: 2px; height: 185px;
    background: var(--rule);
  }
  .contact {
    position: absolute;
    left: 461px; top: 314px;
    font-size: 20px;
    font-weight: 600;
    color: var(--ink);
  }
  .contact__address { line-height: 27px; margin-bottom: 4px; }
  .contact__line { display: flex; align-items: center; gap: 8px; line-height: 24px; }
  .contact__icon { width: 13px; height: 13px; flex: none; fill: var(--ink); }
</style>
</head>
<body>
  <div class="card">
    <div class="edge-tab edge-tab--left"></div>
    <div class="edge-tab edge-tab--right"></div>

    <div class="brand">
      <div class="brand__rule"></div>
      <div class="brand__name">The Dashelt Group</div>
      <div class="brand__rule"></div>
    </div>

    <div class="person">
      <div class="person__name">Corinne M Dashelt</div>
      <div class="person__title">President &amp; CEO</div>
    </div>

    <div class="divider"></div>

    <div class="contact">
      <div class="contact__address">
        28516 Belvorne Court<br>
        Harrowfield, DE 19966
      </div>
      <div class="contact__line">
        <svg class="contact__icon" viewBox="0 0 14 14" aria-hidden="true"><rect x="3.5" y="0.5" width="7" height="13" rx="1.5"/><rect x="5" y="2.5" width="4" height="7" fill="#fff"/></svg>
        302.555.0147
      </div>
      <div class="contact__line">
        <svg class="contact__icon" viewBox="0 0 14 14" aria-hidden="true"><rect x="3.5" y="0.5" width="7" height="4"/><rect x="1" y="5" width="12" height="6" rx="1"/><rect x="3.5" y="9" width="7" height="4.5" fill="#fff" stroke="#1f3a8f" stroke-width="1"/></svg>
        302.555.0192
      </div>
      <div class="contact__line">
        <svg class="contact__icon" viewBox="0 0 14 14" aria-hidden="true"><rect x="0.5" y="2.5" width="13" height="9" fill="none" stroke="#1f3a8f" stroke-width="1.3"/><path d="M1 3 L7 8 L13 3" fill="none" stroke="#1f3a8f" stroke-width="1.3"/></svg>
        CDashelt@TheDasheltGroup.example
      </div>
    </div>
  </div>
</body>
</html>
```